Brightgate Automotive Service Website Design

We are working with Brightgate Automotive Service. They are a local mechanic/garage and in need of a new website design.

Some sites to use for inspiration:

https://www.torvalle.example
https://www.quenby.example
https://parks-carcare.example
https://www.hollowmerefullautocare.example/

Thank you for taking the time to consider designing a website for us. We are web developers based in Stockton, CA, USA. Most of our projects go through the same process. Understanding this process may help you win a project with us. We custom-code all of our websites in-house. We don’t have any requirements as to what tools you use for your design, but we prefer Figma files. For any design that we label as four-stars, we send it to the client for review. The client picks the final design they want us to use. Once we complete this process, we will continue to show additional clients all the four-star sites and purchase them later. Your designs will have multiple chances to sell. For better chances of success, we ask that you follow these guidelines.

IMAGES:
If you use any images or icons in the design, we ask that you have a link to the asset so we can purchase the image/icon. Most of the designs we submit do not have the customer’s images on them unless they have some great images. Be creative; show us the feeling you are trying to portray with your image choices. Use any royalty-free site you choose. We subscribe to Adobe and mainly use their images, but we can purchase images outside of Adobe.

PLEASE NOTE: we will not submit designs to clients with watermarks on the images.

FONTS:
We ask that you identify the fonts used in the design. This can be done in a message if you want. We typically use Google Fonts and Adobe Fonts.

CONTENT:
We're always open to different content and ideas. We often submit designs with stock images so the client can see our vision. We typically take pictures after the website launch to use their images with our vision. Lorem Ipsum is fine for paragraphs, but we ask that you write the headers in correct English. We want to be able to show the vision and identify the sections of the website.

INSPIRATION:
We typically add a couple of links in the brief of websites we like to help you get started in your design.

REVISIONS:
We do not often ask for revisions of the designs unless we see something in the design that may not appeal to the client. If there are slight changes that we want to make, we do that in the development process.

FEEDBACK:
We rarely give feedback on designs during the design process. We are working on many website projects and do not have the time to provide feedback. We usually respond if your request is well thought out and asks specific questions, but a note asking “feedback, please” usually goes unanswered.

```html
<!DOCTYPE html>
<html lang="en">
<head>
<meta charset="utf-8">
<title>Brightgate Automotive Service</title>
<link href="https://fonts.googleapis.com/css2?family=Oswald:wght@500;600;700&family=Mulish:wght@400;600;700;800&display=swap" rel="stylesheet">
<style>
:root{
  --red:#a0000b;
  --black:#000;
  --ink:#111;
  --text:#444;
  --grey-logo:#8a8a8a;
  --light:#f1f1f1;
  --white:#fff;
  --line:#555;
}
*{box-sizing:border-box;margin:0;padding:0}
html,body{width:1200px;height:3924px;overflow:hidden;background:var(--white)}
body{position:relative;font-family:'Mulish',sans-serif;color:var(--ink)}
.abs{position:absolute}
.display{font-family:'Oswald',sans-serif;text-transform:uppercase;font-weight:600}
.btn{position:absolute;display:flex;align-items:center;justify-content:center;background:var(--red);color:var(--white);font-family:'Oswald',sans-serif;font-weight:600;text-transform:uppercase;text-decoration:none}
.rule{position:absolute;height:2px;width:58px;background:var(--red)}

/* header */
.site-header{position:absolute;top:0;left:0;width:1200px;height:137px;background:var(--white)}
.logo{position:absolute;font-family:'Oswald',sans-serif;font-weight:700;color:var(--grey-logo);letter-spacing:-1px;line-height:1}
.header-phone{left:716px;top:33px;display:flex;align-items:center;gap:10px;font-size:17px;font-weight:600}
.main-nav{position:absolute;top:81px;left:437px;display:flex;gap:0}
.main-nav a{font-family:'Oswald',sans-serif;font-weight:500;font-size:15px;color:var(--ink);text-decoration:none;text-transform:uppercase;height:32px;display:flex;align-items:center;padding:0 10px;margin-right:22px}
.main-nav a.active{background:var(--red);color:var(--white)}

/* hero */
.hero{position:absolute;top:137px;left:0;width:1200px;height:541px;background:linear-gradient(90deg,#3e4a55 0%,#2a6f94 30%,#1f3d55 55%,#14212c 75%,#0f1820 100%)}
.hero h1{position:absolute;left:716px;top:44px;font-family:'Oswald',sans-serif;font-weight:600;font-size:70px;line-height:76px;color:var(--white);text-transform:uppercase}
.hero p{position:absolute;left:716px;top:290px;width:340px;font-size:21px;line-height:30px;color:var(--white)}
.dots{position:absolute;top:489px;left:556px;display:flex;gap:11px}
.dots span{width:13px;height:13px;border-radius:50%;background:var(--white)}
.dots span.on{background:var(--red)}

/* services */
.section-title{position:absolute;left:0;width:1200px;text-align:center;font-family:'Oswald',sans-serif;font-weight:600;text-transform:uppercase;color:var(--ink)}
.service-card{position:absolute;width:288px;height:271px;border:1px solid #333;background:var(--white);text-align:center}
.service-card svg{position:absolute;left:119px;top:26px}
.service-card h3{position:absolute;top:104px;left:0;width:100%;font-family:'Oswald',sans-serif;font-weight:600;font-size:17px;text-transform:uppercase}
.service-card p{position:absolute;top:141px;left:34px;width:220px;font-size:13px;line-height:19.5px;color:var(--text)}
.service-card a{position:absolute;top:226px;left:50%;transform:translateX(-50%);font-size:12px;font-weight:800;color:var(--red);text-decoration:none;border-bottom:1px solid var(--red);padding:0 6px 6px;white-space:nowrap}
.service-card.featured{background:var(--red);border-color:var(--red);color:var(--white)}
.service-card.featured p,.service-card.featured a{color:var(--white);border-color:var(--white)}
.btn-outline{position:absolute;display:flex;align-items:center;justify-content:center;border:1.5px solid var(--red);color:var(--red);font-family:'Oswald',sans-serif;font-weight:600;font-size:13px;text-transform:uppercase}

/* welcome */
.welcome{position:absolute;top:1540px;left:0;width:1200px;height:490px;background:var(--black)}
.welcome-photo{position:absolute;left:0;top:0;width:640px;height:490px;background:linear-gradient(90deg,#2a4a78 0%,#3a5f8a 40%,#1c2c44 75%,#000 100%)}
.welcome p{position:absolute;left:620px;top:181px;width:432px;font-size:13px;line-height:19.5px;color:#e6e6e6}

/* values */
.values{position:absolute;top:2030px;left:0;width:1200px;height:559px;background:linear-gradient(120deg,#ececec,#f7f7f7 50%,#eaeaea)}
.values-box{position:absolute;left:151px;top:63px;width:898px;height:452px;background:var(--white);box-shadow:0 2px 10px rgba(0,0,0,.06)}
.value{position:absolute;width:240px;text-align:center;top:168px}
.value .icon{width:80px;height:80px;border:2px solid var(--red);border-radius:50%;margin:0 auto;display:flex;align-items:center;justify-content:center}
.value h3{margin-top:34px;font-family:'Oswald',sans-serif;font-weight:600;font-size:18px;text-transform:uppercase}
.value p{margin-top:14px;font-size:13.5px;line-height:18px;color:#777;padding:0 30px}

/* tire */
.tire{position:absolute;top:2589px;left:0;width:1200px;height:350px;background:#1b1f24}
.tire-photo{position:absolute;left:420px;top:0;width:780px;height:350px;background:linear-gradient(90deg,#1b1f24 0%,#2d3238 25%,#3b4047 60%,#5d6670 100%)}
.tire h2{position:absolute;left:145px;top:44px;font-family:'Oswald',sans-serif;font-weight:600;font-size:38px;line-height:43px;color:var(--white);text-transform:uppercase}
.tire p{position:absolute;left:145px;top:196px;width:340px;font-size:12.5px;line-height:18px;color:#ddd}

/* articles */
.article{position:absolute;top:3099px;width:285px}
.article .thumb{width:285px;height:244px}
.article .kicker{margin-top:24px;font-size:13px;font-weight:800;color:var(--red)}
.article h3{margin-top:10px;font-size:17.5px;line-height:22px;font-weight:800;color:var(--ink)}

/* footer */
.site-footer{position:absolute;top:3582px;left:0;width:1200px;height:342px;background:var(--black);color:var(--white)}
.footer-col h4{font-family:'Mulish',sans-serif;font-weight:800;font-size:15px;text-transform:uppercase}
.footer-col ul{list-style:none;margin-top:16px}
.footer-col li{font-size:12.5px;line-height:18px}
.contact-item{display:flex;gap:14px;margin-top:14px;font-size:12.5px;line-height:17px}
.socials{display:flex;gap:5px;margin-top:18px}
.socials span{width:30px;height:30px;border-radius:50%;background:var(--white)}
.footer-rule{position:absolute;left:151px;top:241px;width:898px;height:1px;background:#444}
.copyright{position:absolute;left:0;top:279px;width:1200px;text-align:center;font-size:11.5px}
</style>
</head>
<body>

<header class="site-header">
  <div class="logo" style="left:149px;top:34px;font-size:54px">BRIGHTGATE</div>
  <div class="abs header-phone">
    <svg width="22" height="22" viewBox="0 0 24 24" fill="none" stroke="#111" stroke-width="1.8"><path d="M5 3h4l2 5-2.5 1.5a11 11 0 0 0 6 6L16 13l5 2v4a2 2 0 0 1-2 2A17 17 0 0 1 3 5a2 2 0 0 1 2-2z"/></svg>
    +1 555 014 2290
  </div>
  <a class="btn" style="left:892px;top:27px;width:159px;height:37px;font-size:13px">Make an Appointment</a>
  <nav class="main-nav">
    <a class="active">Home</a><a>About Us</a><a>Services</a><a>Vehicles</a><a>Specials</a><a>Reviews</a><a style="margin-right:0">Contact Us</a>
  </nav>
</header>

<section class="hero">
  <div class="abs" role="img" aria-label="Mechanic leaning over an open car engine bay with a work light in a garage" style="inset:0"></div>
  <h1>Local.<br>Reliable.<br>Auto Care.</h1>
  <p>Reliable repairs and maintenance from the neighborhood mechanic you can trust.</p>
  <a class="btn" style="left:716px;top:414px;width:219px;height:50px;font-size:18px">Make an Appointment</a>
  <div class="dots"><span class="on"></span><span></span><span></span><span></span></div>
</section>

<section>
  <h2 class="section-title" style="top:722px;font-size:36px">Auto Repair Services</h2>
  <div class="rule" style="left:571px;top:798px"></div>

  <article class="service-card" style="left:151px;top:847px">
    <svg width="50" height="50" viewBox="0 0 50 50" fill="none" stroke="#a0000b" stroke-width="2.5"><path d="M4 14l8 2h10l6 4 14-6-8 14H14l-4-10z"/><path d="M16 12h6"/><path d="M43 30c0 3-2 5-3 5s-3-2-3-5l3-4z" fill="#a0000b"/></svg>
    <h3>Oil Change</h3>
    <p>Sed ut perspiciatis unde omnis iste natus error sit voluptatem accu santium doloremque lauda.</p>
    <a>Oil Change Services &nbsp;↗</a>
  </article>
  <article class="service-card featured" style="left:457px;top:847px">
    <svg width="50" height="50" viewBox="0 0 50 50" fill="none" stroke="#fff" stroke-width="2.5"><path d="M6 44l6-6M10 34l16-16 6 6-16 16z"/><path d="M30 16l8-8V4M38 8h6"/></svg>
    <h3>Exhaust &amp; Mufflers</h3>
    <p>Sed ut perspiciatis unde omnis iste natus error sit voluptatem accu santium doloremque lauda.</p>
    <a>Exhaust &amp; Muffler Services &nbsp;↗</a>
  </article>
  <article class="service-card" style="left:762px;top:847px">
    <svg width="50" height="50" viewBox="0 0 50 50" fill="none" stroke="#a0000b" stroke-width="2.5"><circle cx="25" cy="25" r="22"/><circle cx="25" cy="25" r="8"/><path d="M10 16a17 17 0 0 1 14-9"/></svg>
    <h3>Brakes</h3>
    <p>Sed ut perspiciatis unde omnis iste natus error sit voluptatem accu santium doloremque lauda.</p>
    <a>Brake Repair Services &nbsp;↗</a>
  </article>
  <article class="service-card" style="left:151px;top:1141px">
    <svg width="50" height="50" viewBox="0 0 50 50"><circle cx="25" cy="25" r="22" fill="#a0000b"/><circle cx="25" cy="25" r="9" fill="#fff"/><circle cx="25" cy="25" r="4" fill="#a0000b"/></svg>
    <h3>Tires &amp; Wheels</h3>
    <p>Sed ut perspiciatis unde omnis iste natus error sit voluptatem accu santium doloremque lauda.</p>
    <a>Tire &amp; Wheel Services &nbsp;↗</a>
  </article>
  <article class="service-card" style="left:457px;top:1141px">
    <svg width="50" height="50" viewBox="0 0 50 50" fill="none" stroke="#a0000b" stroke-width="3"><path d="M25 3v44M6 14l38 22M6 36l38-22"/><path d="M19 6l6 5 6-5M19 44l6-5 6 5"/></svg>
    <h3>A/C</h3>
    <p>Sed ut perspiciatis unde omnis iste natus error sit voluptatem accu santium doloremque lauda.</p>
    <a>A/C Repair Services &nbsp;&nbsp;&nbsp;&nbsp;&nbsp;&nbsp;&nbsp;↗</a>
  </article>
  <article class="service-card" style="left:762px;top:1141px">
    <svg width="50" height="50" viewBox="0 0 50 50" fill="none" stroke="#a0000b" stroke-width="2.5"><circle cx="25" cy="25" r="22"/><circle cx="25" cy="25" r="16"/><path d="M9 22h32M25 29v12"/><circle cx="25" cy="25" r="4"/></svg>
    <h3>Steering &amp; Suspension</h3>
    <p>Sed ut perspiciatis unde omnis iste natus error sit voluptatem accu santium doloremque lauda.</p>
    <a>Steering &amp; Suspension Services &nbsp;↗</a>
  </article>

  <a class="btn-outline" style="left:530px;top:1454px;width:140px;height:37px">See All Services</a>
</section>

<section class="welcome">
  <div class="welcome-photo" role="img" aria-label="Mechanic in blue overalls working with a wrench underneath a lifted car"></div>
  <div class="abs display" style="left:617px;top:42px;font-size:22px;color:#fff">Welcome to</div>
  <div class="abs display" style="left:617px;top:66px;font-size:56px;line-height:1;color:var(--red)">Brightgate</div>
  <div class="rule" style="left:620px;top:149px"></div>
  <p>At vero eos et accusamus et iusto odio dignissimos ducimus qui blanditiis praesentium voluptatum deleniti atque corrupti quos dolores et quas molestias excepturi sint occaecati cupiditate non provident, similique sunt in culpa qui officia deserunt mollitia animi, id est laborum et dolorum fuga. Et harum quidem rerum facilis est et expedita distinctio. Nam libero tempore, cum soluta nobis est eligendi optio cumque nihil impedit quo minus id quod maxime placeat facere possimus, omnis voluptas assumenda est, omnis dolor repellendus. Temporibus autem quibusdam et aut officiis debitis aut rerum necessitatibus saepe eveniet ut et voluptates.</p>
  <a class="btn" style="left:621px;top:400px;width:113px;height:32px;font-size:14px">Read More</a>
</section>

<section class="values">
  <div class="values-box">
    <h2 class="section-title" style="left:0;width:898px;top:42px;font-size:37px">Complete Auto Care, It's What We're All About</h2>
    <div class="rule" style="left:420px;top:115px"></div>
    <div class="value" style="left:45px">
      <div class="icon"><svg width="40" height="40" viewBox="0 0 40 40" fill="none" stroke="#a0000b" stroke-width="2.5"><circle cx="20" cy="22" r="8"/><circle cx="20" cy="22" r="3"/><path d="M12 10a8 8 0 0 1 16 0zM20 10v-6"/><path d="M8 34l6-6M32 34l-6-6"/></svg></div>
      <h3>3,500+ Technicians</h3>
      <p>At vero eos et accusamus et iusto odio dignissimos ducimus qui blanditiis praesentium voluptatum deleniti atque corrupti quos dolores et quas molestias.</p>
    </div>
    <div class="value" style="left:329px">
      <div class="icon"><svg width="36" height="36" viewBox="0 0 36 36" fill="#a0000b"><rect x="4" y="16" width="7" height="16"/><path d="M13 16l6-12c3 0 4 2 3 5l-1 5h9c2 0 3 2 2 4l-3 11c0 2-2 3-4 3H13z"/></svg></div>
      <h3>Triple Promise</h3>
      <p>At vero eos et accusamus et iusto odio dignissimos ducimus qui blanditiis praesentium voluptatum deleniti atque corrupti quos dolores et quas molestias.</p>
    </div>
    <div class="value" style="left:613px">
      <div class="icon"><svg width="40" height="40" viewBox="0 0 40 40" fill="#a0000b"><circle cx="20" cy="14" r="5"/><circle cx="9" cy="18" r="4"/><circle cx="31" cy="18" r="4"/><path d="M12 34c0-7 4-11 8-11s8 4 8 11z"/><path d="M3 32c0-5 3-8 6-8 2 0 3 1 4 2-1 2-2 4-2 6zM37 32c0-5-3-8-6-8-2 0-3 1-4 2 1 2 2 4 2 6z"/></svg></div>
      <h3>Satisfaction</h3>
      <p>At vero eos et accusamus et iusto odio dignissimos ducimus qui blanditiis praesentium voluptatum deleniti atque corrupti quos dolores et quas molestias.</p>
    </div>
  </div>
</section>

<section class="tire">
  <div class="tire-photo" role="img" aria-label="Gloved hands holding a new car tire with deep tread"></div>
  <h2>The Tire Advisor:<br>Everything You Need<br>to Know</h2>
  <p>At vero eos et accusamus et iusto odio dignissimos ducimus qui blanditiis praesentium voluptatum deleniti atque corrupti quos dolores et quas molestias.</p>
  <a class="btn" style="left:149px;top:271px;width:111px;height:34px;font-size:14px">Read More</a>
</section>

<section>
  <h2 class="section-title" style="top:2987px;font-size:36px">Auto Care Tips &amp; Advice</h2>
  <div class="rule" style="left:571px;top:3057px"></div>
  <article class="article" style="left:148px">
    <div class="thumb" role="img" aria-label="Technician checking under the hood of a car in a workshop" style="background:linear-gradient(135deg,#9aa3ad,#3c4a5c 60%,#6d7580)"></div>
    <div class="kicker">Lorem Ipsum</div>
    <h3>Sed ut perspiciatis unde omnis iste natus error sit volup</h3>
  </article>
  <article class="article" style="left:457px">
    <div class="thumb" role="img" aria-label="Gloved hands working on engine parts" style="background:linear-gradient(135deg,#3a3a3a,#7a5a3c 45%,#d0701e 60%,#2b2b2b)"></div>
    <div class="kicker">Lorem Ipsum</div>
    <h3>Sed ut perspiciatis unde omnis iste natus error sit volup</h3>
  </article>
  <article class="article" style="left:768px">
    <div class="thumb" role="img" aria-label="Mechanic shaking hands with a customer in a service bay" style="background:linear-gradient(135deg,#c9ccd1,#4a6a94 50%,#2c3c58)"></div>
    <div class="kicker">Lorem Ipsum</div>
    <h3>Sed ut perspiciatis unde omnis iste natus error sit volup</h3>
  </article>
  <a class="btn" style="left:522px;top:3482px;width:156px;height:38px;font-size:15px">View All Articles</a>
</section>

<footer class="site-footer">
  <div class="logo" style="left:149px;top:64px;font-size:54px">BRIGHTGATE</div>
  <div class="abs footer-col" style="left:457px;top:55px">
    <h4>Menu</h4>
    <ul><li>Home</li><li>About Us</li><li>Services</li><li>Vehicles</li><li>Specials</li><li>Reviews</li><li>Contact Us</li></ul>
  </div>
  <div class="abs footer-col" style="left:602px;top:55px">
    <h4>Contact Us</h4>
    <div class="contact-item" style="margin-top:16px">
      <svg width="18" height="18" viewBox="0 0 24 24" fill="#fff" style="margin-top:8px"><path d="M5 3h4l2 5-2.5 1.5a11 11 0 0 0 6 6L16 13l5 2v4a2 2 0 0 1-2 2A17 17 0 0 1 3 5a2 2 0 0 1 2-2z"/></svg>
      <div>Call us<br>+1 555 014 2290</div>
    </div>
    <div class="contact-item">
      <svg width="18" height="14" viewBox="0 0 24 18" fill="#fff" style="margin-top:9px"><path d="M0 0h24v18H0z"/><path d="M1 1l11 9 11-9" stroke="#000" stroke-width="2" fill="none"/></svg>
      <div>Email us<br>info@brightgate.example</div>
    </div>
  </div>
  <div class="abs footer-col" style="left:835px;top:55px">
    <h4>Follow Us</h4>
    <div class="socials"><span></span><span></span><span></span><span></span><span></span></div>
  </div>
  <div class="footer-rule"></div>
  <div class="copyright">Copyright © 2025 All Rights Reserved</div>
</footer>

</body>
</html>
```